Young company in the agrifood product sector *

Our company% 26 # 233; t% 26 # 233; Fernlow Crest low% 26 # 233; % 26 # 224; Toulouse et sp% 26 # 233; cialis% 26 # 233; in the packaging and marketing of beehive products, We need a design of% 26 # 39;% 26 # 39;% 26 # 233; label for honey jar of 250g, The% 26 # 233; labels destiny% 26 # 233; the honey jars will be transparent so that the nectar is visible from the front, our Fernlow Crest logo must be% 26 # 234; be located% 26 # 233; above / middle of% 26 # 393% label followed below the appellation, for example Ch% 26 # 226; taignier followed below the country of% 26 # 39; origin France tracking below r% 26 # 233; region of r% 26 # 233; colte Midi-Pyr% 26 # 233; n% 26 # 233; es and below l% 26 # 39;% 26 # 233; label weight 250g and% 26lt;% 26lt;% 26lt; Honey% 26gt;% 26gt; on the% 26 # 39;% 26 # 233; label will be a plus but optional, The dimensions of the% 26 # 39;% 26 # 233; label are the following 6cm x 6cm. The design must inspire quality% 26 # 233; luxury, l% 26 # 39;% 26 # 233; l% 26 # 233; elegance and confidence, these are quality honey% 26 # 233; and rare honeys from around the world which are very expensive. Very important, the honeys have different colors, this can range from white to orange yellow or darker shades of brown% 26 # 234; black, that's why we would like to have at least 3 colors for light honey, medium dark% 26 # 233; and dark% 26 # 233 ;, Regarding the colors you have free choice of course% 26 # 251; r taking into account the colors of the honey which must% 26 # 234; be visible% 26 # 224; through the% 26 # 39;% 26 # 233; transparent label You will find attached the files of our Fernlow Crest logo. 20%% 26 # 224; 40% transparency on the% 26 # 39;% 26 # 233; label would be reasonable but% 26 # 224; you to see which is better, thanks
- Krone one

```html
<!DOCTYPE html>
<html lang="fr">
<head>
<meta charset="utf-8">
<title>Fernlow Crest — étiquettes miel 250g</title>
<link href="https://fonts.googleapis.com/css2?family=Barlow+Condensed:wght@400;600;700&family=Archivo+Narrow:wght@400;600&display=swap" rel="stylesheet">
<style>
  :root {
    --canvas: #ffffff;
    --honey-top: #f18a1d;
    --honey-bottom: #faa833;
    --teal: #5cc4bb;
    --teal-deep: #39a9a0;
    --ink-light: #ffffff;
    --ink-dark: #15172a;
    --accent-orange: #f39a2a;
  }
  * { box-sizing: border-box; margin: 0; padding: 0; }
  html, body {
    width: 1200px; height: 1200px; overflow: hidden;
    background: var(--canvas);
  }
  .sheet {
    position: relative; width: 1200px; height: 1200px;
    display: flex; justify-content: center; align-items: center; gap: 80px;
  }
  .label-set { position: relative; width: 460px; display: flex; flex-direction: column; align-items: center; }
  .seal-tab {
    width: 86px; height: 110px; background: var(--teal);
    display: flex; flex-direction: column; align-items: center; justify-content: flex-end;
    padding-bottom: 12px; gap: 6px;
    font-family: "Barlow Condensed", sans-serif; font-weight: 600;
    color: var(--ink-light); font-size: 20px; line-height: 0.95; text-align: center;
  }
  .seal-tab .dot { width: 14px; height: 14px; border-radius: 50%; background: var(--ink-light); }
  .label {
    position: relative; width: 460px; height: 460px;
    background: linear-gradient(180deg, var(--honey-top), var(--honey-bottom));
    padding: 10px;
  }
  .label-frame {
    position: relative; width: 100%; height: 100%;
    border: 1.5px solid var(--ink); padding: 22px 18px 0;
    display: flex; flex-direction: column;
  }
  .label--light { --ink: var(--ink-light); --bar-text: var(--accent-orange); }
  .label--dark { --ink: var(--ink-dark); --bar-text: var(--accent-orange); }
  .wordmark {
    font-family: "Barlow Condensed", sans-serif; font-weight: 700;
    color: var(--ink); line-height: 0.86;
  }
  .wordmark-top { display: flex; align-items: center; gap: 14px; font-size: 108px; }
  .wordmark-mark { width: 104px; height: 104px; border-radius: 50%; background: var(--ink); flex: none; }
  .wordmark-bottom { font-size: 160px; text-align: right; padding-right: 4px; margin-top: 4px; }
  .appellation {
    align-self: center; margin-top: 10px;
    width: 300px; height: 22px; background: var(--ink);
    font-family: "Archivo Narrow", sans-serif; font-weight: 600;
    color: var(--bar-text); font-size: 16px; letter-spacing: 2px;
    text-align: center; line-height: 22px;
  }
  .pattern-band {
    margin: 14px -18px 0; height: 30px;
    background: linear-gradient(180deg, var(--teal) 0%, var(--teal-deep) 50%, #ffffff 100%);
  }
  .origin-row {
    margin: 0 -18px; padding: 8px 10px 0;
    display: flex; justify-content: space-between; align-items: baseline;
    font-family: "Archivo Narrow", sans-serif; color: var(--ink);
  }
  .origin-row .country { font-size: 22px; font-weight: 400; }
  .origin-row .weight { font-size: 22px; font-weight: 400; }
  .origin-row .region { font-size: 17px; font-weight: 400; }
</style>
</head>
<body>
  <main class="sheet">
    <section class="label-set">
      <div class="seal-tab"><span class="dot"></span><span>Fernlow<br>Crest</span></div>
      <article class="label label--light">
        <div class="label-frame">
          <div class="wordmark">
            <div class="wordmark-top"><span class="wordmark-mark"></span><span>Fernlow</span></div>
            <div class="wordmark-bottom">Crest</div>
          </div>
          <div class="appellation">Chataîgnier</div>
          <div class="pattern-band" role="img" aria-label="Teal zigzag decorative band"></div>
          <div class="origin-row">
            <span class="country">FRANCE</span>
            <span class="weight">250g</span>
            <span class="region">Midi-Pyrénées</span>
          </div>
        </div>
      </article>
    </section>

    <section class="label-set">
      <div class="seal-tab"><span class="dot"></span><span>Fernlow<br>Crest</span></div>
      <article class="label label--dark">
        <div class="label-frame">
          <div class="wordmark">
            <div class="wordmark-top"><span class="wordmark-mark"></span><span>Fernlow</span></div>
            <div class="wordmark-bottom">Crest</div>
          </div>
          <div class="appellation">Chataîgnier</div>
          <div class="pattern-band" role="img" aria-label="Teal zigzag decorative band"></div>
          <div class="origin-row">
            <span class="country">FRANCE</span>
            <span class="weight">250g</span>
            <span class="region">Midi-Pyrénées</span>
          </div>
        </div>
      </article>
    </section>
  </main>
</body>
</html>
```